Il Bel Gatto Leaf Design Business Card/Hang Tag

Design a 3.5" X 2" (Leaf Shaped-See Files) Business Card/ Hang Tag that will have our Business Logo and Info on the Front, and will have On-Line Delivery Logos and Info on the Rear.

```html
<!DOCTYPE html>
<html lang="en">
<head>
<meta charset="utf-8">
<title>Il Bel Gatto – Business Card / Hang Tag</title>
<link rel="stylesheet" href="https://fonts.googleapis.com/css2?family=Montserrat:wght@400;500;700&display=swap">
<style>
  :root {
    --bg: #f3ebe0;
    --red: #d9163c;
    --paper: #f6f6f4;
    --green: #2f7a3c;
    --green-dark: #1f5a2a;
    --rose: #c9243a;
    --ink-red: #d9163c;
  }
  * { box-sizing: border-box; margin: 0; padding: 0; }
  html, body { width: 1200px; height: 1200px; overflow: hidden; }
  body {
    background: var(--bg);
    font-family: "Montserrat", Arial, sans-serif;
    display: flex; flex-direction: column; align-items: center; justify-content: center;
    gap: 70px;
  }
  .card {
    width: 700px; height: 400px;
    background: var(--red);
    border-radius: 0 190px 0 190px;
    padding: 26px;
    box-shadow: 0 14px 30px rgba(120, 80, 40, 0.12);
  }
  .card-face {
    width: 100%; height: 100%;
    background: var(--paper);
    border-radius: 0 165px 0 165px;
    position: relative;
    display: flex;
  }

  /* logo block */
  .logo { display: flex; flex-direction: column; align-items: center; }
  .logo-art {
    width: 230px; height: 120px;
    border-radius: 60px 60px 20px 20px;
    background: radial-gradient(ellipse at center, #ffffff 30%, #6aa35c 62%, var(--green-dark) 100%);
  }
  .logo-name {
    margin-top: 10px;
    font-size: 26px; font-weight: 700; color: var(--ink-red);
    letter-spacing: 1px;
  }
  .logo-sub {
    font-size: 13px; font-weight: 500; color: var(--green);
    letter-spacing: 3px; text-transform: uppercase;
  }
  .logo-info {
    margin-top: 8px; padding-top: 6px;
    border-top: 1px solid var(--green);
    text-align: center; line-height: 1.45;
    font-size: 11px; color: var(--green);
  }
  .logo-info .web { color: var(--ink-red); font-weight: 500; }

  /* front */
  .front .card-face { align-items: center; justify-content: center; }

  /* back */
  .back .brand-side {
    width: 56%; display: flex; align-items: center; justify-content: center; gap: 26px;
    padding-left: 30px;
  }
  .delivery { display: flex; flex-direction: column; gap: 22px; }
  .partner { display: flex; align-items: center; gap: 8px; font-size: 12px; font-weight: 500; color: var(--ink-red); }
  .partner .dot { width: 16px; height: 16px; border-radius: 50%; background: var(--ink-red); }
  .partner.alt { color: var(--green); }
  .partner.alt .dot { background: var(--green); }
  .back .logo-art { width: 190px; height: 100px; }
  .back .logo-name { font-size: 22px; }

  .person-side {
    flex: 1; position: relative;
    display: flex; flex-direction: column; justify-content: center;
    padding-left: 34px;
    color: var(--ink-red);
  }
  .person-side::before {
    content: ""; position: absolute; left: 0; top: 70px; bottom: 90px;
    width: 2px; background: var(--ink-red);
  }
  .person-name { font-size: 26px; font-weight: 500; letter-spacing: 5px; }
  .person-role { font-size: 15px; letter-spacing: 2px; margin-bottom: 26px; }
  .person-contact { font-size: 15px; letter-spacing: 1.5px; line-height: 1.55; }
</style>
</head>
<body>

  <section class="card back">
    <div class="card-face">
      <div class="brand-side">
        <div class="delivery">
          <div class="partner"><span class="dot"></span>Forkrun</div>
          <div class="partner alt"><span class="dot"></span>RideBite</div>
          <div class="partner"><span class="dot"></span>Tablepost</div>
        </div>
        <div class="logo">
          <div class="logo-art" role="img" aria-label="Striped awning framed by a wreath of ivy leaves and red roses with music notes"></div>
          <div class="logo-name">Il Bel Gatto</div>
          <div class="logo-sub">Restaurant</div>
          <div class="logo-info">
            <div class="web">www.ilbelgattoristorante.com</div>
            <div>418 Linden Ave</div>
            <div>Belmont, California 94002</div>
            <div>(650) 555-0148</div>
          </div>
        </div>
      </div>
      <div class="person-side">
        <div class="person-name">JOHN DOE</div>
        <div class="person-role">manager</div>
        <div class="person-contact">
          <div>(650) 555-0148</div>
          <div>418 Linden Ave</div>
          <div>Belmont, California 94002</div>
        </div>
      </div>
    </div>
  </section>

  <section class="card front">
    <div class="card-face">
      <div class="logo">
        <div class="logo-art" role="img" aria-label="Striped awning framed by a wreath of ivy leaves and red roses with music notes"></div>
        <div class="logo-name">Il Bel Gatto</div>
        <div class="logo-sub">Restaurant</div>
        <div class="logo-info">
          <div class="web">www.ilbelgattoristorante.com</div>
          <div>418 Linden Ave</div>
          <div>Belmont, California 94002</div>
          <div>(650) 555-0148</div>
        </div>
      </div>
    </div>
  </section>

</body>
</html>
```